A5 Flyer for Financial Services Business

I am after a re-design of our business flyer to fit in with our new branding style and logo colour scheme. Wanting something with a bit of designer flair that I could not create myself. I have included the flyer which I created which lacks style so dazzle me.

I want to use the same content.

Text for main body of flyer is

Are you a small business owner, tradie or PAVC Service Provider struggling to stay on top of your bookkeeping and compliance obligations? If so we would love to help you get back on track and take control of your business finances so that you can make informed business decisions and focus on what you do best.

We have over 20 years industry experience and, as a small business ourselves, we are able to offer our clients a personal bookkeeping solution tailored to meet the needs of your business.

Accounts Payable | Accounts Receivable
Customer Invoicing
Bank and Credit Card Reconciliations
Payroll | Superannuation | Payroll Tax
Business Activity | Instalment Activity Statements
Regular Financial Reports
Ledgera and Tallybook Set-Up and Training

```html
<!DOCTYPE html>
<html lang="en">
<head>
<meta charset="utf-8">
<title>Even Keel Bookkeeping Services – A5 Flyer</title>
<link href="https://fonts.googleapis.com/css2?family=Carlito:wght@400;700&family=Source+Sans+3:wght@400;600&display=swap" rel="stylesheet">
<style>
  :root{
    --teal:#0f8f92;
    --teal-dark:#0b7478;
    --teal-soft:#9fcfce;
    --ink:#1c1c1c;
    --grey:#555a5e;
    --stage:#a8a9ad;
    --paper:#ffffff;
  }
  html,body{margin:0;width:1200px;height:1200px;overflow:hidden;background:var(--stage);}
  .flyer{
    position:absolute;left:205px;top:40px;width:951px;height:1350px;
    background:var(--paper);transform:scale(0.8296);transform-origin:0 0;overflow:hidden;
    font-family:"Source Sans 3",sans-serif;color:var(--ink);
  }
  .hero-art{position:absolute;left:0;top:0;}
  .brand{position:absolute;left:600px;top:168px;width:340px;text-align:center;}
  .brand-name{display:flex;align-items:center;justify-content:center;gap:10px;
    font-family:"Carlito",sans-serif;font-weight:700;font-size:44px;line-height:48px;color:var(--teal);letter-spacing:1px;}
  .brand-dot{width:16px;height:16px;border-radius:50%;background:var(--teal);}
  .brand-sub{font-family:"Carlito",sans-serif;font-size:20px;letter-spacing:7px;color:var(--grey);margin-top:2px;}
  .brand-rule{position:absolute;left:599px;top:272px;width:335px;height:2px;background:var(--teal);}
  .tagline{position:absolute;left:604px;top:288px;width:340px;text-align:center;
    font-size:28px;line-height:35px;color:var(--grey);}
  .intro{position:absolute;left:64px;top:736px;width:824px;font-size:21.5px;line-height:27px;text-align:justify;}
  .intro p{margin:0 0 27px;}
  .services-band{position:absolute;left:0;top:0;}
  .services{position:absolute;left:50px;top:968px;width:845px;height:267px;background:var(--paper);
    border:3px solid var(--teal);border-radius:30px;}
  .service-list{position:absolute;left:0;right:0;top:14px;margin:0;padding:0;list-style:none;text-align:center;
    font-family:"Carlito",sans-serif;font-weight:700;font-size:22.5px;line-height:27.2px;color:var(--teal);}
  .registration{position:absolute;left:22px;top:20px;width:104px;text-align:center;
    font-family:"Carlito",sans-serif;font-size:12px;line-height:15px;}
  .registration-badge{width:100px;height:100px;border-radius:50%;background:var(--teal-soft);margin:0 auto 20px;}
  .accreditation{position:absolute;top:222px;display:flex;align-items:center;gap:20px;
    font-family:"Carlito",sans-serif;font-weight:700;font-size:22px;line-height:28px;}
  .accreditation.first{left:78px;}
  .accreditation.second{left:491px;}
  .diamond{width:16px;height:16px;transform:rotate(45deg);}
  .diamond.grey{background:#8c8c8c;}
  .diamond.teal{background:var(--teal);}
  .contact-col{position:absolute;top:1268px;height:66px;color:#fff;
    font-family:"Carlito",sans-serif;font-weight:700;font-size:19px;}
  .contact-col.address{left:24px;width:200px;}
  .contact-col.online{left:282px;width:430px;}
  .contact-col.phone{left:742px;width:190px;}
  .divider{position:absolute;top:1268px;width:2px;height:62px;background:#fff;}
  .divider.one{left:244px;}
  .divider.two{left:726px;}
  .contact-row{display:flex;align-items:center;gap:8px;height:26px;}
  .contact-row + .contact-row{margin-top:10px;}
  .contact-row.indent{padding-left:30px;}
  .icon{width:22px;height:22px;flex:none;}
</style>
</head>
<body>
<div class="flyer">
  <svg class="hero-art" width="951" height="760" viewBox="0 0 951 760">
    <defs>
      <linearGradient id="heroTone" x1="0" y1="0" x2="1" y2="1">
        <stop offset="0" stop-color="#c9c36a"/>
        <stop offset="0.35" stop-color="#6f7a70"/>
        <stop offset="0.7" stop-color="#c99a86"/>
        <stop offset="1" stop-color="#2f3a5a"/>
      </linearGradient>
      <linearGradient id="teamTone" x1="0" y1="0" x2="1" y2="1"><stop offset="0" stop-color="#8fa3b8"/><stop offset="1" stop-color="#3d4656"/></linearGradient>
      <linearGradient id="meetTone" x1="0" y1="0" x2="1" y2="1"><stop offset="0" stop-color="#e8e6e0"/><stop offset="1" stop-color="#2e3440"/></linearGradient>
      <linearGradient id="tillTone" x1="0" y1="0" x2="1" y2="1"><stop offset="0" stop-color="#c7a45c"/><stop offset="1" stop-color="#3c4a52"/></linearGradient>
    </defs>
    <rect width="951" height="560" fill="url(#heroTone)" role="img" aria-label="Photo: hands pointing at a touchscreen terminal"/>
    <path d="M0,400 Q320,640 951,420 L951,560 Q320,760 0,520 Z" fill="var(--teal)"/>
    <path d="M0,470 Q320,720 951,500 L951,760 L0,760 Z" fill="var(--paper)"/>
    <circle cx="850" cy="200" r="279" fill="var(--paper)" stroke="var(--teal)" stroke-width="4"/>
    <circle cx="161" cy="515" r="137" fill="url(#teamTone)" stroke="var(--teal)" stroke-width="3" role="img" aria-label="Photo: smiling business team giving thumbs up"/>
    <circle cx="463" cy="578" r="137" fill="url(#meetTone)" stroke="var(--teal)" stroke-width="3" role="img" aria-label="Photo: three women reviewing work on a laptop"/>
    <circle cx="775" cy="513" r="137" fill="url(#tillTone)" stroke="var(--teal)" stroke-width="3" role="img" aria-label="Photo: hand using a point-of-sale screen"/>
  </svg>

  <div class="brand">
    <div class="brand-name"><span class="brand-dot"></span>EVEN KEEL</div>
    <div class="brand-sub">Bookkeeping Services</div>
  </div>
  <div class="brand-rule"></div>
  <div class="tagline">Bookkeping Tailored to<br>Your Business Needs</div>

  <div class="intro">
    <p>Are you a small business owner, tradie or PAVC Service Provider struggling to stay on top of your bookkeeping and compliance obligations? If so we would love to help you get back on track and take control of your business finances so that you can make informed business decisions and focus on what you do best.</p>
    <p>We have over 20 years industry experience and, as a small business ourselves, we are able to offer our clients a personal bookkeeping solution tailored to meet the needs of your business.</p>
  </div>

  <svg class="services-band" width="951" height="1350" viewBox="0 0 951 1350">
    <path d="M0,1148 L50,1100 L901,1100 L951,1148 L951,1350 L0,1350 Z" fill="var(--teal)"/>
  </svg>

  <div class="services">
    <div class="registration">
      <div class="registration-badge" role="img" aria-label="Registration badge"></div>
      BAS agent<br>10482736
    </div>
    <ul class="service-list">
      <li>Accounts Payable | Accounts Receivable</li>
      <li>Customer Invoicing</li>
      <li>Bank and Credit Card Reconciliations</li>
      <li>Payroll | Superannuation | Payroll Tax</li>
      <li>Business Activity | Instalment Activity Statements</li>
      <li>Regular Financial Reports</li>
      <li>Ledgera and Tallybook Set-Up and Training</li>
    </ul>
    <div class="accreditation first"><span class="diamond grey"></span>Ledgera Certified Advisor</div>
    <div class="accreditation second"><span class="diamond teal"></span>Tallybook Pro Advisor</div>
  </div>

  <div class="contact-col address">
    <div class="contact-row">
      <svg class="icon" viewBox="0 0 24 24"><circle cx="12" cy="12" r="11" fill="none" stroke="#fff" stroke-width="1.6"/><path d="M12 5a4.5 4.5 0 0 0-4.5 4.5C7.5 13 12 19 12 19s4.5-6 4.5-9.5A4.5 4.5 0 0 0 12 5zm0 6.2a1.7 1.7 0 1 1 0-3.4 1.7 1.7 0 0 1 0 3.4z" fill="#fff"/></svg>
      PO Box 482
    </div>
    <div class="contact-row indent">Lakeview NSW 2999</div>
  </div>
  <div class="divider one"></div>
  <div class="contact-col online">
    <div class="contact-row">
      <svg class="icon" viewBox="0 0 24 24"><circle cx="12" cy="12" r="11" fill="none" stroke="#fff" stroke-width="1.6"/><rect x="6.5" y="8" width="11" height="8" fill="none" stroke="#fff" stroke-width="1.5"/><path d="M6.5 8l5.5 4.5L17.5 8" fill="none" stroke="#fff" stroke-width="1.5"/></svg>
      hello@evenkeelbookkeeping.com.au
    </div>
    <div class="contact-row">
      <svg class="icon" viewBox="0 0 24 24"><circle cx="12" cy="12" r="11" fill="none" stroke="#fff" stroke-width="1.6"/><circle cx="12" cy="12" r="6" fill="none" stroke="#fff" stroke-width="1.4"/><path d="M6 12h12M12 6c-2.5 3-2.5 9 0 12M12 6c2.5 3 2.5 9 0 12" fill="none" stroke="#fff" stroke-width="1.2"/></svg>
      www.evenkeelbookkeeping.com.au
    </div>
  </div>
  <div class="divider two"></div>
  <div class="contact-col phone">
    <div class="contact-row">
      <svg class="icon" viewBox="0 0 24 24"><circle cx="12" cy="12" r="11" fill="none" stroke="#fff" stroke-width="1.6"/><path d="M8.5 6.5l2 2.5-1.2 1.4a7 7 0 0 0 4.3 4.3l1.4-1.2 2.5 2-1.2 1.8c-4.5 0-9.6-5.1-9.6-9.6z" fill="#fff"/></svg>
      0400 123 456
    </div>
  </div>
</div>
</body>
</html>
```